イメージとしましては
添付①のロゴを使用していただき、
重厚感と高級感のあるものにしていただければと思っております。
イメージカラーは添付②の現名刺をご参考にしていただければと思います。

また関連会社の「株式会社MapleCrest研究所」(添付③)の名刺
と両面刷りにすることを考えていますので関連性がある
イメージにしていただけば幸いです。
役職/名前/E-Mail/携帯電話/会社名/住所/電話/FAX/全体E-Mail/URL
緑系、黄・オレンジ系
• 高解像度JPG (.jpg)
• イラストレーター形式 (.ai)
• フォトショップ形式 (.psd)
• PNG形式 (.png)
税理士法人のロゴはあるのでそちらを使用してください(添付①)
ロゴのRGB(53,109,60  255,170,1)
現名刺デザイン添付しますのでイメージの参考にしてください(添付②)
両面刷りにする予定の名刺も添付します(添付③)
添付①の保存バージョンをさげてみました。
開けなかった方は再度ご確認お願いします。
関連会社の「株式会社MapleCrest研究所」(添付③)の名刺と
両面刷りにすることを考えていますが「税理士法人Maple Crest」の方は
「株式会社MapleCrest研究所」と同じようなデザインでいくことはあまり考えておりません。
表裏で関連性の感じられる、または表裏としたときにユニークさがあるようなデザインが
可能でしたらお願いいたします。
また、表裏としたときに裏の「株式会社MapleCrest研究所」の色の部分から表側に例えば円形のグラデーションとかそういったものも見てみたいのでご提案いただけるかた宜しくお願い致します。
皆様たくさんご提案いただきましてありがとうございます。
一部のご提案にだけではありますが
社内で上がった意見をご提案のコメント欄に入れさせていただきました。
ご参考にしていただければ幸いです。

表裏の関連性が非常よくでていたため選定となりました。

裏の名刺のデザインが決まっている状況で多くの提案をしていただきありがとうございました。
いろいろと難しい点はあったかと思います。深く御礼申し上げます。

```html
<!DOCTYPE html>
<html lang="ja">
<head>
<meta charset="utf-8">
<title>名刺 両面デザイン</title>
<link rel="stylesheet" href="https://fonts.googleapis.com/css2?family=Noto+Sans+JP:wght@400;700&family=Noto+Serif+JP:wght@500;700&display=swap">
<style>
:root{
  --green:#356d3c;
  --green-deep:#26532c;
  --gold:#ffaa01;
  --ink:#2b2b2b;
  --paper:#ffffff;
  --backdrop:#ececec;
}
*{margin:0;padding:0;box-sizing:border-box}
html,body{width:847px;height:1200px;overflow:hidden;background:var(--backdrop)}
body{position:relative;font-family:"Noto Sans JP",sans-serif;color:var(--ink)}
.card{position:absolute;left:70px;width:707px;height:440px;background:var(--paper);box-shadow:0 3px 10px rgba(0,0,0,.25);overflow:hidden}
.card--lab{top:70px}
.card--tax{top:620px}
.band{position:absolute;left:0;top:0;width:100%;height:100%}
.title{position:absolute;font-size:13px;letter-spacing:.05em}
.name{position:absolute;font-family:"Noto Serif JP",serif;font-weight:700;font-size:40px;letter-spacing:.18em}
.contact{position:absolute;font-size:15px;line-height:26px}
.contact svg{vertical-align:-3px;margin-right:6px}
.brand{position:absolute;display:flex;align-items:center;gap:12px;font-family:"Noto Serif JP",serif;font-weight:700;color:var(--green)}
.brand-mark{width:40px;height:40px;background:var(--gold)}
.green-text{position:absolute;color:#fff;font-size:15px;line-height:26px;letter-spacing:.03em}
.green-text .org{font-family:"Noto Serif JP",serif;font-weight:700;font-size:27px;line-height:44px;margin-bottom:10px}
.pair span{display:inline-block;min-width:210px}
</style>
</head>
<body>

<section class="card card--lab">
  <svg class="band" viewBox="0 0 707 440" role="img" aria-label="濃い緑の地紋模様の帯">
    <defs>
      <linearGradient id="labGreen" x1="0" y1="0" x2="1" y2="1">
        <stop offset="0" stop-color="#3b7742"/>
        <stop offset="1" stop-color="#26532c"/>
      </linearGradient>
    </defs>
    <path d="M0 232 Q330 188 707 212 L707 440 L0 440 Z" fill="url(#labGreen)"/>
    <path d="M0 232 Q330 188 707 212" fill="none" stroke="var(--gold)" stroke-width="6"/>
  </svg>
  <p class="title" style="left:42px;top:34px">代表取締役</p>
  <p class="name" style="left:40px;top:52px">森田 和真</p>
  <div class="contact" style="left:42px;top:112px">
    <p><svg width="12" height="14" viewBox="0 0 12 14"><rect x="2" y="0" width="8" height="14" rx="1.5" fill="var(--green)"/></svg>090-0000-1234</p>
    <p><svg width="14" height="11" viewBox="0 0 14 11"><rect width="14" height="11" fill="var(--green)"/><path d="M0 0 L7 6 L14 0" fill="none" stroke="#fff" stroke-width="1.3"/></svg>info@maplecrestlab.co.jp</p>
  </div>
  <div class="brand" style="left:420px;top:82px;font-size:24px">
    <span class="brand-mark"></span><span>株式会社MapleCrest研究所</span>
  </div>
  <div class="green-text" style="left:42px;top:248px">
    <p class="org">株式会社MapleCrest研究所</p>
    <p>〒350-0000　埼玉県比企郡青葉町みどり台一丁目5番地3</p>
    <p class="pair"><span>TEL　0493-00-1200</span>FAX　0493-00-1201</p>
  </div>
</section>

<section class="card card--tax">
  <svg class="band" viewBox="0 0 707 440" role="img" aria-label="濃い緑の地紋模様の帯">
    <defs>
      <linearGradient id="taxGreen" x1="0" y1="0" x2="1" y2="1">
        <stop offset="0" stop-color="#3b7742"/>
        <stop offset="1" stop-color="#26532c"/>
      </linearGradient>
    </defs>
    <rect x="0" y="190" width="707" height="250" fill="url(#taxGreen)"/>
    <rect x="0" y="186" width="707" height="4" fill="var(--gold)"/>
  </svg>
  <p class="title" style="left:42px;top:58px">代表社員税理士</p>
  <p class="name" style="left:40px;top:76px">森田 和真</p>
  <div class="contact" style="left:300px;top:72px">
    <p><svg width="12" height="14" viewBox="0 0 12 14"><rect x="2" y="0" width="8" height="14" rx="1.5" fill="var(--green)"/></svg>090-0000-1234</p>
    <p><svg width="14" height="11" viewBox="0 0 14 11"><rect width="14" height="11" fill="var(--green)"/><path d="M0 0 L7 6 L14 0" fill="none" stroke="#fff" stroke-width="1.3"/></svg>info@maplecrestlab.co.jp</p>
  </div>
  <div class="brand" style="left:540px;top:92px;font-size:22px">
    <span class="brand-mark"></span><span>Maple Crest</span>
  </div>
  <div class="green-text" style="left:42px;top:204px">
    <p class="org">税理士法人 Maple Crest</p>
    <p>〒350-0000　埼玉県比企郡青葉町みどり台一丁目5番地3</p>
    <p class="pair"><span>TEL　0493-00-1200</span>FAX　0493-00-1201</p>
    <p>E-mail　member-all@maplecrest.or.jp</p>
    <p>www.maplecrest.or.jp</p>
  </div>
</section>

</body>
</html>
```